Lustiges Einladungskarten-Design für Feier gesucht
Zielgruppe
private Einladung
Aufgabenstellung
Einladung im Posterformat DIN A2 dass auf DINA A6 (9 einzelne Felder) runter gefaltet werden kann.
Die Einladung soll lustig, witzig und ausgefallen sein - auf keinen Fall klassisch, schnörkelig, spießig.
Die Location soll genannt werden: eine bewirtete Waldhütte im Sauerland, Übernachtungsmöglichkeiten, Beginn der Feier: 18.30 Uhr am 29.09.2018
Es handelt sich um eine Feier zum 50.Geburtstag, zum 46. Geburtstag, zur Hochzeit – aber vor allem feiern wir die das Leben, die Liebe und unsere Freunde.
Es ist eine Grillparty – kein Dresscode, keine Spiele – sondern essen, trinken, feiern, tanzen, Spaß haben.
Gern handlettering , illustriert oder andere kreative Ideen.

```html
<!DOCTYPE html>
<html lang="de">
<head>
<meta charset="utf-8">
<title>Einladung – Bist du Wald?</title>
<link rel="stylesheet" href="https://fonts.googleapis.com/css2?family=Amatic+SC:wght@400;700&display=swap">
<style>
  :root {
    --frame: #e2e4dd;
    --sheet: #e2e4dd;
    --page: #ffffff;
    --ink: #463c37;
    --green: #a6c83a;
    --yellow: #f7cb2c;
  }
  * { box-sizing: border-box; margin: 0; padding: 0; }
  html, body { width: 1200px; height: 1200px; overflow: hidden; background: var(--frame); }
  .canvas {
    position: relative; width: 1200px; height: 1200px;
    border: 17px solid var(--frame); background: var(--page);
    font-family: "Amatic SC", cursive; color: var(--ink);
  }
  .sheet { position: absolute; top: 233px; width: 495px; height: 700px; background: var(--sheet); }
  .sheet--front { left: 68px; }
  .sheet--inside { left: 603px; }
  .t { position: absolute; white-space: nowrap; line-height: 1; font-weight: 700; }
  .t.center { left: 0; right: 0; text-align: center; }
  .g { color: var(--green); }
  .art { position: absolute; border-radius: 10px; background: var(--green); }
  .art--dark { background: linear-gradient(180deg, var(--green) 40%, var(--ink) 40%); }
  .icon { position: absolute; overflow: visible; }
  .fold { position: absolute; top: 0; bottom: 0; width: 1px; background: rgba(70,60,55,.06); }
  .rot-up { transform: rotate(-90deg); transform-origin: center; }
  .rot-down { transform: rotate(90deg); transform-origin: center; }
</style>
</head>
<body>
<svg width="0" height="0" style="position:absolute">
  <defs>
    <symbol id="arrow-yellow" viewBox="0 0 90 60">
      <polygon points="4,22 50,20 48,6 86,30 50,56 50,40 6,42" fill="#f7cb2c" stroke="#463c37" stroke-width="4" stroke-linejoin="round"/>
    </symbol>
  </defs>
</svg>

<div class="canvas">
  <!-- Front page -->
  <section class="sheet sheet--front">
    <div class="art" role="img" aria-label="Illustration: grüner Vogel sitzt auf dem Schriftzug" style="left:217px;top:73px;width:60px;height:55px;border-radius:50% 50% 30% 30%"></div>
    <p class="t center" style="top:120px;font-size:74px">ist <span class="g">das</span> jetzt</p>
    <p class="t center" style="top:220px;font-size:32px">die vorder- oder die rückseite?</p>
    <svg class="icon" style="left:186px;top:277px" width="104" height="78" viewBox="0 0 104 78" role="img" aria-label="Wechselpfeile">
      <path d="M4,30 C20,4 70,0 86,12 L88,0 L102,36 L72,40 L80,28 C60,18 28,18 4,30 Z" fill="#a6c83a" stroke="#463c37" stroke-width="2.5" stroke-linejoin="round"/>
      <path d="M100,50 C84,76 34,80 18,66 L14,78 L2,42 L32,38 L24,50 C44,62 76,62 100,50 Z" fill="#463c37"/>
    </svg>
    <p class="t center" style="top:398px;font-size:36px">eh wurscht weil <span class="g">das</span> wichtige</p>
    <p class="t center" style="top:436px;font-size:62px">steht eh <span class="g">auf der</span></p>
    <p class="t center" style="top:515px;font-size:44px">rück- oder vorderseite</p>
    <svg class="icon" style="left:365px;top:590px" width="78" height="54"><use href="#arrow-yellow"/></svg>
  </section>

  <!-- Inside pages -->
  <section class="sheet sheet--inside">
    <div class="fold" style="left:329px"></div>

    <!-- Column 1 -->
    <p class="t" style="left:23px;top:20px;font-size:74px">Bist</p>
    <div class="art" role="img" aria-label="Illustration: Tannenbaum" style="left:11px;top:94px;width:31px;height:53px;border-radius:40% 40% 6px 6px"></div>
    <p class="t g" style="left:46px;top:100px;font-size:56px">du</p>
    <div class="art" role="img" aria-label="Illustration: Laubbaum" style="left:116px;top:95px;width:37px;height:53px;border-radius:50% 50% 20% 20%"></div>
    <p class="t" style="left:14px;top:152px;font-size:60px">wal<span class="g">d</span>?</p>
    <svg class="icon" style="left:132px;top:212px" width="56" height="37"><use href="#arrow-yellow"/></svg>

    <div class="art" role="img" aria-label="Illustration: Pflänzchen mit Erde" style="left:20px;top:250px;width:28px;height:36px"></div>
    <p class="t" style="left:57px;top:252px;font-size:40px">leben</p>
    <p class="t" style="left:14px;top:298px;font-size:40px"><span class="g">ii</span> freunde</p>
    <svg class="icon" style="left:20px;top:348px" width="32" height="30" viewBox="0 0 32 30" role="img" aria-label="Herz">
      <path d="M16,28 C4,18 1,12 2,8 C3,2 12,0 16,8 C20,0 29,2 30,8 C31,12 28,18 16,28 Z" fill="#a6c83a" stroke="#463c37" stroke-width="2"/>
    </svg>
    <p class="t" style="left:60px;top:344px;font-size:40px">liebe</p>
    <p class="t" style="left:20px;top:397px;font-size:14px;line-height:0.95">wenn dir noch ein weiterer<br>grund zum feiern einfällt:</p>
    <p class="t" style="left:20px;top:424px;font-size:22px">bring ihn mit!!</p>
    <svg class="icon rot-down" style="left:145px;top:430px" width="56" height="37"><use href="#arrow-yellow"/></svg>

    <p class="t" style="left:11px;top:485px;font-size:14px;line-height:1.05">du findest dein auto nicht mehr?<br>oder hast plötzlich 2 davon?</p>
    <div class="art" role="img" aria-label="Illustration: zwei grüne Autos" style="left:35px;top:528px;width:95px;height:26px"></div>
    <p class="t" style="left:7px;top:566px;font-size:32px"><span class="g">dann</span> übernachte</p>
    <p class="t" style="left:18px;top:594px;font-size:34px">besser hier!</p>
    <div class="art art--dark" role="img" aria-label="Illustration: Reisetasche und Haus" style="left:35px;top:632px;width:90px;height:46px"></div>

    <!-- Column 2 -->
    <p class="t" style="left:178px;top:26px;font-size:34px"><span class="g">dann</span> zieh an</p>
    <p class="t" style="left:178px;top:68px;font-size:30px">was <span class="g">du</span> willst!</p>
    <div class="art" role="img" aria-label="Illustration: T-Shirt" style="left:178px;top:104px;width:71px;height:56px"></div>
    <div class="art" role="img" aria-label="Illustration: Krone" style="left:271px;top:98px;width:32px;height:32px"></div>
    <div class="art" role="img" aria-label="Illustration: Fliege" style="left:256px;top:132px;width:53px;height:30px"></div>
    <p class="t" style="left:184px;top:170px;font-size:44px">oder nix</p>
    <svg class="icon rot-down" style="left:308px;top:211px" width="56" height="37"><use href="#arrow-yellow"/></svg>

    <div class="art" role="img" aria-label="Illustration: Vogel auf Nest" style="left:228px;top:257px;width:44px;height:75px;border-radius:45%"></div>
    <p class="t rot-up" style="left:196px;top:357px;width:100px;text-align:center;font-size:76px">18.<span class="g">3</span>0</p>

    <div class="art" role="img" aria-label="Illustration: zeigende Hand" style="left:194px;top:496px;width:40px;height:59px"></div>
    <p class="t" style="left:188px;top:560px;font-size:34px">essen</p>
    <p class="t" style="left:188px;top:601px;font-size:34px">feiern</p>
    <p class="t" style="left:188px;top:644px;font-size:34px">trinken</p>
    <p class="t rot-down" style="left:193px;top:560px;width:190px;text-align:center;font-size:46px">spass haben</p>
    <svg class="icon" style="left:321px;top:644px" width="56" height="37"><use href="#arrow-yellow"/></svg>

    <!-- Column 3 -->
    <p class="t" style="left:343px;top:12px;font-size:28px">egal wie</p>
    <svg class="icon" style="left:448px;top:18px" width="18" height="18" role="img" aria-label="Uhr"><circle cx="9" cy="9" r="8" fill="#a6c83a" stroke="#463c37" stroke-width="1.5"/><path d="M9,4 V9 H13" stroke="#463c37" stroke-width="1.5" fill="none"/></svg>
    <p class="t" style="left:343px;top:40px;font-size:32px">aber komm zur</p>
    <div class="art" role="img" aria-label="Illustration: Flugzeug, Auto und Fahrrad" style="left:343px;top:82px;width:133px;height:37px"></div>
    <p class="t" style="left:343px;top:132px;font-size:34px">waldhütte im</p>
    <p class="t" style="left:343px;top:160px;font-size:46px">sauerland</p>

    <p class="t" style="left:343px;top:259px;font-size:40px">am besten</p>
    <p class="t" style="left:343px;top:297px;font-size:34px">am 29.9.2018</p>
    <div class="art" role="img" aria-label="Illustration: Kalenderblatt 29. Sept 2018" style="left:387px;top:343px;width:50px;height:62px;border-radius:3px"></div>
    <svg class="icon" style="left:309px;top:374px;transform:scaleX(-1)" width="56" height="37"><use href="#arrow-yellow"/></svg>
    <svg class="icon" style="left:343px;top:430px" width="10" height="15" role="img" aria-label="Glühbirne"><circle cx="5" cy="5" r="4.5" fill="#a6c83a"/><rect x="3" y="10" width="4" height="4" fill="#463c37"/></svg>
    <p class="t" style="left:357px;top:432px;font-size:12px">denn da sind auch die anderen da</p>

    <div class="art" role="img" aria-label="Illustration: Fernglas mit Vogel" style="left:396px;top:536px;width:37px;height:56px"></div>
    <p class="t" style="left:368px;top:601px;font-size:36px">see you</p>
  </section>
</div>
</body>
</html>
```